Corporate Website - KWARTA HOLDINGS, LLC

This Nevada Corporation has several subsidiaries:
T. M. Designs - Interior Design; Commercial, Residential & Hospitality
T. M. Style - Fashion Design & Styling
FERN LOUNGE - Upscale Membership Only Lounge servicing Business Men and women. It is located in Accra, Ghana
FERN SUITES - Full Service Executive Suites for top Businesses. Located in Accra, Ghana.
THE MATERIAL YARD - Distributor for Building and Interior Design Materials
URL: www.kwartaholdingsllc.example
Website: info@kwartaholdingsllc.example
Phones: 1 702-555-0147 Las Vegas; +233 26 5550193 Ghana

Industry/Entity Type

Fashion

```html
<!DOCTYPE html>
<html lang="en">
<head>
<meta charset="utf-8">
<title>KWARTA HOLDINGS, LLC</title>
<link href="https://fonts.googleapis.com/css2?family=Arimo:wght@400;700&family=Ubuntu:wght@400;500&display=swap" rel="stylesheet">
<style>
:root{
  --gold:#a9843f;
  --gold-light:#d2b277;
  --gold-dark:#8a6a2e;
  --ink:#3c3c3c;
  --text:#555555;
  --panel:#efefef;
  --panel-line:#dcdcdc;
  --nav:#e9e9e9;
  --white:#ffffff;
}
*{margin:0;padding:0;box-sizing:border-box}
html,body{width:1200px;height:1000px;overflow:hidden;background:var(--white)}
body{font-family:"Arimo",Arial,sans-serif;color:var(--text);position:relative}
.abs{position:absolute}

/* header */
.brand{left:176px;top:38px;width:240px;display:flex;align-items:center;gap:12px}
.brand-mark{width:26px;height:26px;background:var(--gold);flex:none}
.brand-name{font-family:"Ubuntu",sans-serif;font-weight:500;color:var(--gold);line-height:1.05}
.brand-name .big{display:block;font-size:40px;letter-spacing:1px}
.brand-name .small{display:block;font-size:16px;letter-spacing:1px}

.contact{right:173px;top:20px;text-align:right;font-size:11.5px;line-height:13px;color:var(--ink)}
.contact h2{font-family:"Ubuntu",sans-serif;font-weight:400;font-size:19px;color:var(--gold);margin-bottom:5px}
.contact b{color:var(--gold)}
.contact a{color:var(--gold);font-weight:700;text-decoration:underline}

.btn-gold{background:linear-gradient(#d4b57a,var(--gold) 55%,var(--gold-dark));color:var(--white);border-radius:4px;box-shadow:0 1px 2px rgba(0,0,0,.35)}
.boutique-btn{left:880px;top:91px;width:147px;height:30px;font-family:"Ubuntu",sans-serif;font-size:15px;display:flex;align-items:center;justify-content:center}

/* navigation */
.nav{left:176px;top:143px;width:851px;height:35px;background:linear-gradient(#f8f8f8,var(--nav));border:1px solid #d6d6d6;border-radius:3px}
.nav-item{position:absolute;top:10px;font-size:13px;color:#4a4a4a;transform:translateX(-50%);white-space:nowrap}
.nav-home{left:207px;top:137px;width:77px;height:36px;font-weight:700;font-size:13px;display:flex;align-items:center;justify-content:center;border-radius:3px 3px 4px 4px}

/* slider */
.slider{left:176px;top:180px;width:851px;height:344px;background:var(--white);border:1px solid #d9d9d9;box-shadow:0 10px 14px -10px rgba(0,0,0,.35)}
.slide-photo{left:184px;top:188px;width:835px;height:327px;background:linear-gradient(100deg,#b9b4ad 0%,#e8e3da 30%,#d9c6a4 55%,#c7b58f 70%,#9aa48a 100%)}
.arrow{width:40px;height:80px;top:313px;background:#f4f4f4;box-shadow:0 0 4px rgba(0,0,0,.3)}
.arrow-left{left:184px;border-radius:0 40px 40px 0}
.arrow-right{left:979px;border-radius:40px 0 0 40px;background:linear-gradient(90deg,var(--gold-light),var(--gold))}
.arrow svg{position:absolute;top:30px}
.caption{left:247px;top:373px;width:394px;height:115px;background:rgba(40,40,40,.78);padding:10px 20px 10px 24px}
.caption h3{font-size:24px;font-weight:700;color:var(--white);margin-bottom:6px;white-space:nowrap}
.caption p{font-size:10.6px;line-height:15.5px;color:#f0d9a8}

/* welcome panel */
.welcome{left:176px;top:555px;width:613px;height:341px;background:var(--panel);border:1px solid var(--panel-line);border-radius:4px}
.heading{font-family:"Ubuntu",sans-serif;font-weight:400;color:var(--ink)}
.heading span{color:var(--gold)}
.welcome-title{left:201px;top:568px;font-size:21px}
.dots{border-top:1px dotted #bdbdbd;height:0}
.para{font-size:10.8px;line-height:15.6px;letter-spacing:-0.15px;color:#444}
.photo{border-radius:8px;box-shadow:0 2px 4px rgba(0,0,0,.35)}
.photo-lounge{left:580px;top:616px;width:184px;height:113px;background:linear-gradient(135deg,#e9dcc5,#b89b75 55%,#4b3a2c)}
.photo-fireplace{left:197px;top:763px;width:183px;height:113px;background:linear-gradient(135deg,#5a3d27,#8a6443 50%,#d9cbb4)}
.more{height:23px;width:71px;font-size:11px;font-weight:700;display:flex;align-items:center}
.more .label{flex:1;text-align:center}
.more .chev{width:22px;text-align:center;border-left:1px solid rgba(255,255,255,.6)}

/* side column */
.side-title{left:823px;font-size:24px}
.service-list{left:823px;top:582px;list-style:none}
.service-list li{display:flex;align-items:center;height:21.5px;font-size:10.8px;color:#333;white-space:nowrap}
.service-list svg{margin:0 10px 0 10px}
.designer{left:825px;display:flex;gap:11px;font-size:10.8px;line-height:13px;color:#333}
.avatar{width:30px;height:30px;background:#8a8a8a;border:2px solid #cfcfcf;flex:none}

/* footer */
.footer{left:176px;top:920px;width:851px;height:24px;background:var(--gold);color:var(--white);font-size:11px;display:flex;align-items:center;justify-content:space-between;padding:0 22px 0 28px}
.footer nav a{color:var(--white);text-decoration:none}
.footer nav a.current{text-decoration:underline}
.footer .sep{margin:0 6px}
.footer p{font-weight:700}
</style>
</head>
<body>

<header>
  <div class="abs brand">
    <span class="brand-mark"></span>
    <div class="brand-name"><span class="big">KWARTA</span><span class="small">HOLDINGS, LLC</span></div>
  </div>

  <div class="abs contact">
    <h2>Contact Information</h2>
    <p>Lorem Ipsum is simply dummy</p>
    <p>Phone: <b>1 702-555-0147</b></p>
    <p>Email: <a>info@kwartaholdingsllc.example</a></p>
  </div>
  <div class="abs btn-gold boutique-btn">Online Boutique</div>
</header>

<nav class="abs nav" aria-label="Main">
  <span class="nav-item" style="left:197px">About Us</span>
  <span class="nav-item" style="left:355px">Online Boutique</span>
  <span class="nav-item" style="left:512px">Services</span>
  <span class="nav-item" style="left:637px">Blog</span>
  <span class="nav-item" style="left:769px">Contact Us</span>
</nav>
<div class="abs btn-gold nav-home">Home</div>

<section>
  <div class="abs slider"></div>
  <div class="abs slide-photo" role="img" aria-label="Bright living room with cream leather sofas, a white fireplace and wooden floor"></div>
  <div class="abs arrow arrow-left">
    <svg width="20" height="20" viewBox="0 0 20 20" style="left:10px"><path d="M14 2 L4 10 L14 18 Z" fill="#9a9a9a"/></svg>
  </div>
  <div class="abs arrow arrow-right">
    <svg width="20" height="20" viewBox="0 0 20 20" style="left:12px"><path d="M6 2 L16 10 L6 18 Z" fill="#ffffff"/></svg>
  </div>
  <div class="abs caption">
    <h3>commercial and residential</h3>
    <p>Services provided by our design firm including: commercial and residential interior design and decorating and hardscape restoration as well as realty. Custom furniture, decor, in house upholsterer, seamstress, photographer, etc.</p>
  </div>
</section>

<main>
  <div class="abs welcome"></div>
  <h2 class="abs heading welcome-title">Welcome to <span>Our Company</span></h2>
  <div class="abs dots" style="left:200px;top:599px;width:565px"></div>

  <p class="abs para" style="left:200px;top:613px;width:362px">Lorem ipsum dolor sit amet, consectetuer adipiscing elit, sed diam nonummy nibh euismod tincidunt ut laoreet dolore magna aliquam erat volutpat. Ut wisi enim ad minim veniam, quis nostrud exerci tation ullamcorper suscipit lobortis nisl ut aliquip ex ea commodo consequat. Duis autem vel eum iriure dolor in hendrerit in vulputate velit esse molestie consequat,</p>
  <div class="abs photo photo-lounge" role="img" aria-label="Modern lounge interior with low sofa and warm lighting"></div>
  <div class="abs btn-gold more" style="left:200px;top:707px"><span class="label">More</span><span class="chev">»</span></div>

  <div class="abs dots" style="left:200px;top:744px;width:565px"></div>

  <div class="abs photo photo-fireplace" role="img" aria-label="Dark wood living room with fireplace, lounge chairs and pendant lamp"></div>
  <p class="abs para" style="left:401px;top:762px;width:365px">Lorem ipsum dolor sit amet, consectetuer adipiscing elit, sed diam nonummy nibh euismod tincidunt ut laoreet dolore magna aliquam erat volutpat. Ut wisi enim ad minim veniam, quis nostrud exerci tation ullamcorper suscipit lobortis nisl ut aliquip ex ea commodo consequat. Duis autem vel eum iriure dolor in hendrerit in vulputate velit esse molestie consequat,</p>
  <div class="abs btn-gold more" style="left:401px;top:854px"><span class="label">More</span><span class="chev">»</span></div>
</main>

<aside>
  <h2 class="abs heading side-title" style="top:549px">Our <span>Services</span></h2>
  <ul class="abs service-list">
    <li><svg width="16" height="16" viewBox="0 0 16 16"><circle cx="8" cy="8" r="8" fill="#a9843f"/><path d="M4.5 8.2 L7 10.6 L11.6 5.6" stroke="#fff" stroke-width="2" fill="none"/></svg>Commercial Design</li>
    <li><svg width="16" height="16" viewBox="0 0 16 16"><circle cx="8" cy="8" r="8" fill="#a9843f"/><path d="M4.5 8.2 L7 10.6 L11.6 5.6" stroke="#fff" stroke-width="2" fill="none"/></svg>Residential Interior Design</li>
    <li><svg width="16" height="16" viewBox="0 0 16 16"><circle cx="8" cy="8" r="8" fill="#a9843f"/><path d="M4.5 8.2 L7 10.6 L11.6 5.6" stroke="#fff" stroke-width="2" fill="none"/></svg>Decorating, Hardscape Restoration</li>
    <li><svg width="16" height="16" viewBox="0 0 16 16"><circle cx="8" cy="8" r="8" fill="#a9843f"/><path d="M4.5 8.2 L7 10.6 L11.6 5.6" stroke="#fff" stroke-width="2" fill="none"/></svg>Realty, Custom furniture, decor</li>
  </ul>
  <div class="abs btn-gold more" style="left:823px;top:675px"><span class="label">More</span><span class="chev">»</span></div>
  <div class="abs dots" style="left:823px;top:708px;width:204px"></div>

  <h2 class="abs heading side-title" style="top:711px">Our <span>Designers</span></h2>
  <div class="abs designer" style="top:743px"><span class="avatar"></span><p>Lorem ipsum dolor sit amet,<br>consectetuer adipiscing</p></div>
  <div class="abs designer" style="top:787px"><span class="avatar"></span><p>Lorem ipsum dolor sit amet,<br>consectetuer</p></div>
  <div class="abs designer" style="top:830px"><span class="avatar"></span><p>Lorem ipsum dolor sit<br>amet, consectetuer adipiscing</p></div>
  <div class="abs btn-gold more" style="left:823px;top:873px"><span class="label">More</span><span class="chev">»</span></div>
</aside>

<footer class="abs footer">
  <nav>
    <a>Home</a><span class="sep">|</span><a class="current">About Us</a><span class="sep">|</span><a>Online Boutique</a><span class="sep">|</span><a>Services</a><span class="sep">|</span><a>Blog</a><span class="sep">|</span><a>Contact Us</a>
  </nav>
  <p>©Copyright 2015 KWARTA HOLDINGS, LLC All Right Reserved.</p>
</footer>

</body>
</html>
```